Real Estate Business Cards

Looking for a clean, sharp and professional look for our Real Estate investment Fund that invests in Multi Family Apartment buildings.

Target Market(s)

Real Estate Fund

Industry/Entity Type

Real Estate

Contact Information for Business Card

Company Description: Real Estate Investment Fund
Company Name: RKW Holdings
Name: Marcus Olvane
Cell: (917) 482-0657
Email: marcus@rkwholdings-example.com
Website: www.rkwholdings-example.com
Address: 418, 9th Street, Brooklyn NY 11218

Colors

Designer to choose colors to be used in the design.

Requirements
Nice to have
• Colors to match logo

```html
<!DOCTYPE html>
<html lang="en">
<head>
<meta charset="utf-8">
<title>RKW Holdings – Business Card</title>
<link href="https://fonts.googleapis.com/css2?family=Lato:wght@400;700;900&display=swap" rel="stylesheet">
<style>
  :root {
    --brand-blue: #0a6db4;
    --brand-blue-light: #1398d3;
    --brand-grey: #4a4a4c;
    --text-grey: #3d3d3f;
    --card-white: #ffffff;
    --page-bg: #e9ecef;
  }
  * { margin: 0; padding: 0; box-sizing: border-box; }
  html, body {
    width: 1200px; height: 900px; overflow: hidden;
    background: var(--page-bg);
    font-family: 'Lato', sans-serif;
  }
  .canvas { position: relative; width: 1200px; height: 900px; }
  .card {
    position: absolute; left: 280px; width: 640px; height: 360px;
    overflow: hidden;
    box-shadow: 0 6px 18px rgba(0,0,0,0.18);
  }

  /* Back side */
  .card-back {
    top: 50px;
    background: linear-gradient(160deg, var(--brand-blue) 0%, #0b78bd 55%, var(--brand-blue-light) 100%);
  }
  .back-emblem {
    position: absolute; left: 320px; top: 180px; width: 230px; height: 230px;
    margin: -115px 0 0 -115px; border-radius: 50%;
    background: var(--card-white);
    display: flex; align-items: center; justify-content: center; gap: 10px;
  }
  .brand-name {
    color: var(--brand-blue); font-weight: 400; text-transform: uppercase;
    letter-spacing: 2px; white-space: nowrap;
  }
  .back-emblem .brand-name { font-size: 22px; }
  .brand-square { background: var(--brand-blue); flex: none; }
  .back-emblem .brand-square { width: 16px; height: 16px; }

  /* Front side */
  .card-front { top: 490px; background: var(--card-white); }
  .front-brand {
    position: absolute; left: 90px; top: 70px;
    display: flex; align-items: center; gap: 12px;
  }
  .front-brand .brand-name { font-size: 30px; }
  .front-brand .brand-square { width: 20px; height: 20px; }

  .front-bands { position: absolute; left: 0; top: 0; width: 640px; height: 360px; }
  .website {
    position: absolute; left: 24px; top: 266px;
    color: var(--card-white); font-size: 18px; letter-spacing: 0.5px;
  }

  .contact {
    position: absolute; right: 30px; top: 118px; text-align: right;
  }
  .contact-name {
    color: var(--brand-blue); font-weight: 900; font-size: 27px;
    letter-spacing: 1px; margin-bottom: 10px;
  }
  .contact-line {
    display: flex; justify-content: flex-end; align-items: center; gap: 8px;
    color: var(--text-grey); font-size: 17px; line-height: 26px; letter-spacing: 0.5px;
  }
  .contact-line svg { width: 16px; height: 16px; fill: var(--brand-blue); }
  .contact-address {
    margin-top: 6px; padding-right: 24px;
    color: var(--brand-blue); font-size: 18px; line-height: 24px; letter-spacing: 0.8px;
  }
</style>
</head>
<body>
<main class="canvas">

  <section class="card card-back" aria-label="Card back">
    <div class="back-emblem">
      <span class="brand-square"></span>
      <span class="brand-name">RKW Holdings</span>
    </div>
  </section>

  <section class="card card-front" aria-label="Card front">
    <svg class="front-bands" viewBox="0 0 640 360" aria-hidden="true">
      <polygon points="0,245 336,245 350,330 640,330 640,360 0,360" fill="var(--brand-blue)"/>
      <polygon points="348,300 640,300 640,318 351,318" fill="var(--brand-grey)"/>
    </svg>

    <div class="front-brand">
      <span class="brand-square"></span>
      <span class="brand-name">RKW Holdings</span>
    </div>

    <p class="website">www.rkwholdings-example.com</p>

    <div class="contact">
      <p class="contact-name">Marcus Olvane</p>
      <p class="contact-line">(917) 482-0657
        <svg viewBox="0 0 24 24" aria-hidden="true"><path d="M6.6 10.8a15 15 0 0 0 6.6 6.6l2.2-2.2a1 1 0 0 1 1-.25 11.4 11.4 0 0 0 3.6.57 1 1 0 0 1 1 1V20a1 1 0 0 1-1 1A17 17 0 0 1 3 4a1 1 0 0 1 1-1h3.5a1 1 0 0 1 1 1c0 1.25.2 2.45.57 3.57a1 1 0 0 1-.25 1z"/></svg>
      </p>
      <p class="contact-line">marcus@rkwholdings-example.com
        <svg viewBox="0 0 24 24" aria-hidden="true"><path d="M2 5h20v14H2z M2 5l10 8 10-8" fill="var(--brand-blue)" stroke="#fff" stroke-width="1.5"/></svg>
      </p>
      <p class="contact-address">418, 9th Street<br>Brooklyn NY 11218</p>
    </div>
  </section>

</main>
</body>
</html>
```